Local snack brand needs a WordPress theme design

We need a custom WordPress theme for a new Australian snack company called Crunchwell. Based in Coffs Harbour, we create functional food snacks using local bananas and other produce. The theme should reflect our community-first philosophy and local roots, featuring an aerial banner of the region’s banana plantations and images of growers harvesting bananas.
The design should include layouts for:
1. Bio pages (profile photo and blurb)
2. Product pages (packaging, nutrition information panel, ingredients, 3. product description, health claim badges like “source of fibre” and “good source of potassium,” and awards)
4. Where to Buy page (interactive map, market stall imagery)
5. Blog posts (feature image, paragraph, quotes)
The final theme should use Crunchwell’s vector logo in the header (without text), and Crunchwell name (in brand font) in the footer. Should be modern, responsive design (mobile first). It should have a grass roots feel, be clean and feel good, leverage the brand colours, but still feel professional (to reflect a horticulturist and nutritionist), and be flexible for future updates. The successful design needs to be delivered as an installable theme in ZIP archive.
Please visit our website and read our pages to get a feel for "us". See https://crunchwell-example.au/
1 week extension for the 3 finalists to respond to feedback and make their final submissions before awarding 1st, 2nd and 3rd.
Local, health-conscious, athletes, busy parents, active minds
Food wholesaler, health & nutrition, agribusiness / local produce
- Galano Grotesque Bold

```html
<!DOCTYPE html>
<html lang="en">
<head>
<meta charset="utf-8">
<title>Crunchwell — The Science of Functional Snacking</title>
<link rel="stylesheet" href="https://fonts.googleapis.com/css2?family=Poppins:wght@400;500;600;700&family=Arimo:wght@400;700&display=swap">
<style>
:root{
  --green:#6a9a3f;
  --green-dark:#5c8a34;
  --green-pale:#d9e6cc;
  --ink:#111111;
  --text:#222222;
  --grey-bg:#f6f6f6;
  --black:#0b0b0b;
  --white:#ffffff;
  --cream:#f3f0d2;
}
*{box-sizing:border-box;margin:0;padding:0}
html,body{width:1200px;height:4739px;overflow:hidden}
body{font-family:"Arimo",Arial,sans-serif;color:var(--text);background:var(--white);position:relative}
.heading{font-family:"Poppins",sans-serif;font-weight:700;letter-spacing:-0.5px;color:var(--ink)}
.heading .accent{color:var(--green)}
.photo{position:absolute}
.btn{position:absolute;display:flex;align-items:center;justify-content:center;border-radius:30px;font-family:"Poppins",sans-serif;font-weight:600;font-size:14px;text-transform:uppercase;text-decoration:none}
.btn-solid{background:var(--green);color:var(--white)}
.btn-outline{border:2px solid var(--white);color:var(--white)}

/* top bar + nav */
.top-bar{position:absolute;left:0;top:0;width:1200px;height:41px;background:var(--green);color:var(--white);font-family:"Poppins",sans-serif;font-size:14px}
.top-bar .welcome{position:absolute;left:127px;top:12px}
.top-bar .mail{position:absolute;right:127px;top:12px;display:flex;align-items:center;gap:8px}
.site-nav{position:absolute;left:0;top:41px;width:1200px;height:88px;background:var(--white)}
.site-nav a{position:absolute;top:36px;font-family:"Poppins",sans-serif;font-weight:500;font-size:13px;color:var(--ink);text-decoration:none}
.brand-badge{position:absolute;left:544px;top:0;width:112px;height:112px;border-radius:50%;background:var(--white)}
.brand-name{position:absolute;left:0;width:1200px;top:86px;text-align:center;font-family:"Poppins",sans-serif;font-weight:700;font-size:21px;color:var(--ink)}
.brand-dot{position:absolute;left:578px;top:20px;width:44px;height:44px;border-radius:50%;background:var(--green)}

/* hero */
.hero{position:absolute;left:0;top:129px;width:1200px;height:622px;background:radial-gradient(ellipse at center,#26292a 0%,#1a1c1c 55%,#3a3222 100%);overflow:hidden}
.hero .mark{position:absolute;left:555px;top:160px;width:90px;height:90px;border-radius:50%;background:var(--green)}
.hero h1{position:absolute;left:0;width:1200px;top:330px;text-align:center;font-family:"Poppins",sans-serif;font-weight:700;font-size:68px;letter-spacing:2px;color:var(--white)}
.hero p{position:absolute;left:0;width:1200px;top:420px;text-align:center;font-family:"Poppins",sans-serif;font-size:29px;color:var(--white);letter-spacing:0.5px}

/* welcome */
.welcome-title{position:absolute;left:0;width:1200px;top:820px;text-align:center;font-size:44px}
.welcome-sub{position:absolute;left:0;width:1200px;top:898px;text-align:center;font-weight:700;font-size:19px;line-height:26px;color:var(--ink)}
.welcome-mark{position:absolute;left:127px;top:1003px;width:400px;height:424px;display:flex;flex-direction:column;align-items:center;justify-content:center;gap:28px}
.welcome-mark .circle{width:300px;height:300px;border-radius:50%;background:var(--green)}
.welcome-mark .name{font-family:"Poppins",sans-serif;font-weight:700;font-size:40px;color:var(--green)}
.welcome-copy{position:absolute;left:581px;top:1010px;width:505px;font-size:16px;line-height:20px}
.welcome-copy p{margin-bottom:20px}

/* snacks */
.snacks{position:absolute;left:0;top:1542px;width:1200px;height:635px;background:var(--grey-bg)}
.snacks h2{position:absolute;left:0;width:1200px;top:92px;text-align:center;font-size:44px}
.snack{position:absolute;top:184px;width:260px;text-align:center}
.snack .thumb{width:222px;height:222px;border-radius:50%;margin:0 auto}
.snack h3{margin-top:32px;font-family:"Poppins",sans-serif;font-weight:600;font-size:19px;color:var(--ink)}
.snack p{margin-top:4px;font-size:15px;line-height:18px;color:#444}

/* where to buy */
.buy-title{position:absolute;left:127px;top:2307px;font-size:44px}
.buy-sub{position:absolute;left:129px;top:2383px;font-family:"Arimo",sans-serif;font-size:23px;color:var(--ink)}
.buy-copy{position:absolute;left:129px;top:2434px;width:430px;font-size:15.5px;line-height:20px}
.buy-copy p{margin-bottom:20px}
.fade-ring{position:absolute;border-radius:50%;background:var(--green-pale);opacity:.55}

/* story */
.story{position:absolute;left:0;top:2880px;width:1200px;height:511px;background:var(--grey-bg)}
.story-grid .photo{border:4px solid var(--white)}
.story-title{position:absolute;left:668px;top:2944px;font-size:44px}
.story-copy{position:absolute;left:670px;top:3020px;width:400px;font-size:15.5px;line-height:20px}
.story-copy p{margin-bottom:20px}

/* cta band */
.cta{position:absolute;left:0;top:3467px;width:1200px;height:351px;background:var(--green)}
.cta p{position:absolute;left:0;width:1200px;top:98px;text-align:center;font-family:"Poppins",sans-serif;font-weight:600;font-size:26px;line-height:41px;color:var(--cream)}

/* follow */
.follow-title{position:absolute;left:0;width:1200px;top:3900px;text-align:center;font-size:35px;line-height:42px}
.follow-grid .photo{top:4021px;width:223px;height:276px}

/* footer */
.site-footer{position:absolute;left:0;top:4389px;width:1200px;height:350px;background:var(--black);color:var(--white)}
.footer-brand .dot{position:absolute;left:224px;top:62px;width:44px;height:44px;border-radius:50%;background:var(--green)}
.footer-brand .name{position:absolute;left:127px;top:158px;font-family:"Poppins",sans-serif;font-weight:700;font-size:29px}
.footer-heading{position:absolute;top:58px;font-family:"Poppins",sans-serif;font-weight:600;font-size:19px}
.footer-links{position:absolute;list-style:none;font-family:"Poppins",sans-serif;font-size:16px;line-height:29px}
.footer-links a{color:var(--white);text-decoration:none}
.mail-input{position:absolute;left:808px;top:103px;width:267px;height:44px;border-radius:22px;background:var(--white);color:#333;font-family:"Poppins",sans-serif;font-size:13px;padding:14px 20px}
.mail-btn{left:808px;top:160px;width:267px;height:44px}
.footer-rule{position:absolute;left:127px;top:267px;width:946px;height:1px;background:#3a3a3a}
.copyright{position:absolute;left:0;width:1200px;top:302px;text-align:center;font-family:"Poppins",sans-serif;font-size:14px}
</style>
</head>
<body>

<header>
  <div class="top-bar">
    <span class="welcome">Welcome to Crunchwell</span>
    <span class="mail">
      <svg width="14" height="11" viewBox="0 0 14 11" aria-hidden="true"><rect x="0.5" y="0.5" width="13" height="10" rx="1" fill="#fff"/><path d="M1 1l6 5 6-5" stroke="#6a9a3f" stroke-width="1.4" fill="none"/></svg>
      hello@crunchwell-example.au
    </span>
  </div>
  <nav class="site-nav">
    <a style="left:136px" href="#">HOME</a>
    <a style="left:210px" href="#">ABOUT US</a>
    <a style="left:315px" href="#">OUR INGREDIENTS</a>
    <a style="left:755px" href="#">OUR SNACKS</a>
    <a style="left:882px" href="#">BLOG</a>
    <a style="left:951px" href="#">WHERE TO BUY</a>
  </nav>
  <div class="brand-badge"></div>
  <span class="brand-dot"></span>
  <div class="brand-name">CRUNCHWELL</div>
</header>

<section class="hero">
  <div class="photo" role="img" aria-label="Dried banana chips scattered on a dark slate surface" style="left:0;top:0;width:1200px;height:622px"></div>
  <span class="mark"></span>
  <h1>CRUNCHWELL</h1>
  <p>The Science of Functional Snacking</p>
</section>

<main>
  <h2 class="heading welcome-title"><span class="accent">WELCOME TO</span> CRUNCHWELL</h2>
  <p class="welcome-sub">The science of functional snacking — grown,<br>crafted and shared on the Coffs Coast.</p>
  <div class="welcome-mark">
    <span class="circle"></span>
    <span class="name">Crunchwell</span>
  </div>
  <div class="welcome-copy">
    <p>We’re Sam &amp; Lewis — a grower and a nutritionist — combining our love of real food and sustainable practice to create something a little different. Crunchwell is where fresh thinking meets rescued produce, and where small batches are made with big purpose.</p>
    <p>From dehydrated bananas topped with coconut (our signature Cocobana), to chia fruit rolls and functional snack bars, everything we make starts with whole ingredients and is formulated to nourish. Designed for athletes, busy parents, active minds, and good eaters of all kinds.</p>
    <p>We source imperfect or surplus fruit from growers on the Mid North Coast and turn it into smart, real-food snacks — thoughtfully balanced for energy, performance and taste. Every recipe is developed with both horticultural and nutritional care, supporting gut health, steady energy, and minimal waste.</p>
    <p>Whether you’re fuelling your next ride, packing school lunches, or just looking for something better in the snack aisle, we’re glad you found us.</p>
  </div>

  <section class="snacks">
    <h2 class="heading"><span class="accent">OUR</span> SNACKS</h2>
    <div class="snack" style="left:85px">
      <div class="thumb" role="img" aria-label="Banana chips with coconut on a green leaf" style="background:radial-gradient(circle,#e9d99a 0%,#8bb06a 60%,#2f6a45 100%)"></div>
      <h3>COCOBANA</h3><p>Banana +<br>desiccated coconut</p>
    </div>
    <div class="snack" style="left:341px">
      <div class="thumb" role="img" aria-label="Banana chips dusted with cinnamon and coconut" style="background:radial-gradient(circle,#f3e6c4 0%,#d9b47a 60%,#8a5a33 100%)"></div>
      <h3>CINNABANA</h3><p>Banana +<br>desiccated coconut</p>
    </div>
    <div class="snack" style="left:597px">
      <div class="thumb" role="img" aria-label="Bowl of banana slices with macadamia crumb" style="background:radial-gradient(circle,#f1e2a8 0%,#a57c4c 60%,#3b2a1e 100%)"></div>
      <h3>MACABANA</h3><p>Banana + roasted<br>macadamia crumb</p>
    </div>
    <div class="snack" style="left:854px">
      <div class="thumb" role="img" aria-label="Banana coffee smoothie with bananas and coffee beans" style="background:radial-gradient(circle,#d9b48a 0%,#c9a46a 45%,#5a3b25 100%)"></div>
      <h3>BANOFFEE</h3><p>Banana +<br>ground coffee</p>
    </div>
  </section>

  <section class="where-to-buy">
    <h2 class="heading buy-title">WHERE TO <span class="accent">BUY</span></h2>
    <p class="buy-sub">Find us by the beach every Sunday</p>
    <div class="buy-copy">
      <p>You can catch Crunchwell in person every week at the Bayside Growers Market — a beautiful makers and growers market held at the Jetty Foreshore in Coffs Harbour.</p>
      <p>We bring our full range of handcrafted snacks — from our signature Cocobana to functional favourites like Banoffee and Macabana — all made from upcycled local produce, developed by a grower and a nutritionist who care about what you eat and where it comes from.</p>
    </div>
    <a class="btn btn-solid" href="#" style="left:127px;top:2639px;width:164px;height:49px">Order Online</a>
    <span class="fade-ring" style="left:880px;top:2330px;width:270px;height:400px"></span>
    <div class="photo" role="img" aria-label="Bowl of porridge topped with banana slices, chocolate and mint" style="left:705px;top:2298px;width:362px;height:362px;border-radius:50%;background:radial-gradient(circle at 55% 45%,#f4ead0 0%,#c9ad86 45%,#6e8f5a 85%,#4c6e3d 100%)"></div>
    <div class="photo" role="img" aria-label="Close-up of golden banana chips" style="left:662px;top:2495px;width:207px;height:205px;border-radius:50%;border:4px solid #fff;background:radial-gradient(circle,#f3d27a 0%,#e1a640 60%,#b97a2a 100%);box-shadow:0 4px 14px rgba(0,0,0,.15)"></div>
  </section>

  <section class="story"></section>
  <span class="fade-ring" style="left:0;top:2990px;width:330px;height:440px"></span>
  <div class="story-grid">
    <div class="photo" role="img" aria-label="Bowl of yoghurt topped with banana slices" style="left:127px;top:2815px;width:208px;height:196px;background:linear-gradient(135deg,#eef0f2,#d7d3c3)"></div>
    <div class="photo" role="img" aria-label="Banana slices on a rice cake with almonds" style="left:340px;top:2815px;width:208px;height:196px;background:linear-gradient(135deg,#e8d4a3,#9a6e45)"></div>
    <div class="photo" role="img" aria-label="Wooden bowl filled with banana chips" style="left:127px;top:3014px;width:421px;height:245px;background:linear-gradient(135deg,#f0c76a,#b07a38 60%,#5a3f27)"></div>
  </div>
  <h2 class="heading story-title">OUR <span class="accent">STORY</span></h2>
  <div class="story-copy">
    <p>We’re Sam &amp; Lewis — two locals passionate about real food, good soil, and better snacks.</p>
    <p>Crunchwell began as a conversation between a horticulturist and a nutritionist — a grower and a formulator — about how much perfectly good produce never makes it to people’s plates, and how much better snacking could be if we treated it with the same respect we give meals.</p>
  </div>
  <a class="btn btn-solid" href="#" style="left:670px;top:3224px;width:138px;height:48px">Read More</a>

  <section class="cta">
    <p>FOOD THAT’S FORMULATED, NOT FACTORY-MADE.<br>SNACKING THAT FEELS GOOD — IN EVERY SENSE.</p>
    <a class="btn btn-outline" href="#" style="left:495px;top:199px;width:210px;height:47px">Buy the Products</a>
  </section>

  <section class="follow">
    <h2 class="heading follow-title">FOLLOW THE SNACK SYSTEM.<br><span class="accent">JOIN THE CRUNCHWELL.</span></h2>
    <div class="follow-grid">
      <div class="photo" role="img" aria-label="Bowl of banana chips with fresh bananas" style="left:127px;background:linear-gradient(160deg,#f3dc7a,#c98f3f 60%,#6a4328)"></div>
      <div class="photo" role="img" aria-label="Banana chips tumbling onto a pile" style="left:368px;background:linear-gradient(160deg,#f6efe0,#e2b465 60%,#b47a38)"></div>
      <div class="photo" role="img" aria-label="Banana slices on a rice cake with nut butter" style="left:609px;background:linear-gradient(160deg,#d9c7a6,#a98a62 60%,#6d5640)"></div>
      <div class="photo" role="img" aria-label="Layered banana caramel smoothie in a jar" style="left:850px;background:linear-gradient(160deg,#f2eee8,#c99873 55%,#7a4a2c)"></div>
    </div>
  </section>
</main>

<footer class="site-footer">
  <div class="footer-brand">
    <span class="dot"></span>
    <span class="name">CRUNCHWELL</span>
  </div>
  <h4 class="footer-heading" style="left:479px">Links</h4>
  <ul class="footer-links" style="left:480px;top:108px">
    <li><a href="#">Blog</a></li><li><a href="#">About</a></li><li><a href="#">FAQs</a></li><li><a href="#">Authors</a></li>
  </ul>
  <ul class="footer-links" style="left:631px;top:114px">
    <li><a href="#">Events</a></li><li><a href="#">Shop</a></li><li><a href="#">Patterns</a></li><li><a href="#">Themes</a></li>
  </ul>
  <h4 class="footer-heading" style="left:808px">Join our mailing list</h4>
  <div class="mail-input">Email:</div>
  <a class="btn btn-solid mail-btn" href="#">Join Now</a>
  <div class="footer-rule"></div>
  <p class="copyright">Copyright © 2025 Crunchwell. All rights reserved</p>
</footer>

</body>
</html>
```